Business Card design for new private practice opening

I need a business card design for my new private practice with my new logo uploaded as a file
On the front the logo
On the back: maybe a small logo somewhere?
Priv. Doz. DDr. Corinna Vestaluk
Fachärztin für Allgemein- & Viszeralchirurgie
Address: xxx
Tel: xxx
Mobil:xxx
Webseite:xxx
Email:xxx

Contact Information for Business Card

See project description above for details

Requirements
Nice to have
• I would like the colors of the logo incorporated into the business card

```html
<!DOCTYPE html>
<html lang="de">
<head>
<meta charset="utf-8">
<title>Kaldera Chirurgie – Visitenkarte</title>
<link rel="stylesheet" href="https://fonts.googleapis.com/css2?family=Open+Sans:wght@400;700&display=swap">
<style>
  :root {
    --stage: #1c1d1f;
    --teal: #35c6c6;
    --teal-light: #52cbc6;
    --teal-text: #2fb6b4;
    --grey: #8c8c8c;
    --ink: #4a4a4a;
    --paper: #ffffff;
  }
  * { box-sizing: border-box; margin: 0; padding: 0; }
  html, body {
    width: 1200px; height: 840px; overflow: hidden;
    background: var(--stage);
    font-family: "Open Sans", Arial, sans-serif;
  }
  .canvas { position: relative; width: 1200px; height: 840px; }

  .card {
    position: absolute;
    width: 540px; height: 310px;
    border-radius: 22px;
    overflow: hidden;
  }

  /* Front */
  .card-front {
    left: 50px; top: 110px;
    background: linear-gradient(135deg, var(--teal) 0%, var(--teal-light) 100%);
  }
  .front-brand {
    position: absolute; left: 50%; top: 50%;
    transform: translate(-50%, -50%);
    display: flex; align-items: center; gap: 22px;
  }
  .brand-circle {
    width: 92px; height: 92px; border-radius: 50%;
    flex: none;
  }
  .card-front .brand-circle { border: 4px solid var(--paper); }
  .brand-name {
    font-weight: 700; text-transform: uppercase;
    font-size: 34px; line-height: 1.02; letter-spacing: 1px;
  }
  .card-front .brand-name { color: var(--paper); }

  /* Back */
  .card-back {
    left: 610px; top: 420px;
    background: var(--paper);
    border-bottom: 5px solid var(--teal);
  }
  .back-brand {
    position: absolute; right: 40px; top: 30px;
    display: flex; align-items: center; gap: 16px;
  }
  .card-back .brand-circle {
    width: 72px; height: 72px;
    border: 3px solid var(--grey);
  }
  .card-back .brand-name { color: var(--grey); font-size: 27px; }

  .divider-top {
    position: absolute; left: 150px; right: 40px; top: 124px;
    height: 1.5px; background: var(--teal);
  }
  .holder { position: absolute; left: 34px; top: 150px; }
  .holder-name {
    color: var(--teal-text); font-weight: 700; font-size: 19px;
  }
  .holder-title { color: var(--ink); font-size: 13px; margin-top: 1px; }
  .divider-bottom {
    position: absolute; left: 34px; width: 290px; top: 205px;
    height: 1.5px; background: var(--teal);
  }
  .contacts {
    position: absolute; left: 34px; top: 218px;
    list-style: none; color: var(--ink); font-size: 14px;
  }
  .contacts li { display: flex; align-items: center; gap: 8px; line-height: 24px; }
  .contacts svg { width: 14px; height: 14px; flex: none; }
  .address {
    position: absolute; right: 40px; top: 170px;
    text-align: right; color: var(--grey); font-size: 14px; line-height: 1.4;
  }
</style>
</head>
<body>
<main class="canvas">

  <section class="card card-front" aria-label="Vorderseite">
    <div class="front-brand">
      <div class="brand-circle"></div>
      <div class="brand-name">Kaldera<br>Chirurgie</div>
    </div>
  </section>

  <section class="card card-back" aria-label="Rückseite">
    <div class="back-brand">
      <div class="brand-circle"></div>
      <div class="brand-name">Kaldera<br>Chirurgie</div>
    </div>
    <div class="divider-top"></div>

    <div class="holder">
      <p class="holder-name">Priv. Doz. DDr. Corinna Vestaluk</p>
      <p class="holder-title">Fachärztin für Allgemein- &amp; Viszeralchirurgie</p>
    </div>
    <div class="divider-bottom"></div>

    <ul class="contacts">
      <li>
        <svg viewBox="0 0 14 14" aria-hidden="true"><circle cx="7" cy="7" r="7" fill="var(--teal)"/><path d="M4 4.5c.5-.8 1.3-.8 1.6 0l.4 1c.1.4-.3.7-.5.9.4.9 1 1.5 1.9 1.9.2-.2.5-.6.9-.5l1 .4c.8.3.8 1.1 0 1.6-2.6 1.4-6.6-2.6-5.3-5.3z" fill="#fff"/></svg>
        044-123 456 789
      </li>
      <li>
        <svg viewBox="0 0 14 14" aria-hidden="true"><circle cx="7" cy="7" r="7" fill="var(--teal)"/><rect x="3.5" y="4.5" width="7" height="5" fill="#fff"/><path d="M3.5 4.5 7 7.3l3.5-2.8" fill="none" stroke="var(--teal)" stroke-width="0.8"/></svg>
        info@webname.com
      </li>
      <li>
        <svg viewBox="0 0 14 14" aria-hidden="true"><circle cx="7" cy="7" r="7" fill="var(--teal)"/><circle cx="7" cy="7" r="3.6" fill="none" stroke="#fff" stroke-width="0.9"/><path d="M3.4 7h7.2M7 3.4c-1.6 2-1.6 5.2 0 7.2M7 3.4c1.6 2 1.6 5.2 0 7.2" fill="none" stroke="#fff" stroke-width="0.8"/></svg>
        www.websitename.com
      </li>
    </ul>

    <p class="address">Your Address, City<br>State, Zip 0000</p>
  </section>

</main>
</body>
</html>
```